Premium website for 'Kestrel Voyages Elite'

Exclusive Torque League travel packages: world-class tickets, premium hospitality, seamless travel, and curated experiences that bring the spirit of each destination to life.

1. Overall Style and Impression
Aesthetic: Modern, premium, and dynamic, reflecting the speed and excitement of a high-profile sport or event.

Focus: Highly visual and focused on driving users toward specific, high-value conversion points (like finding a race or viewing a premium package).

We need on the homepage a few blocks for all destinations.
One the specific page of the destination, we need a list of tickets.
An example for our website is https://zomerratours.com/

Functional requirements

The web site is designed to deliver an end-to-end Torque League travel experience, combining flight bookings, hotel reservations, and race ticket purchases into one seamless booking process. This system provides a unified API layer that integrates external booking services and enables developers to build, manage, and customize complete travel packages for each TL Grand Prix event.

System Overview

The platform is built around three core microservices, all connected through a central Package API:

1. Flight Booking Service ✈️
Integrates with global flight providers (e.g.,Flyvora API).

2. Hotel Booking Service 🏨
Connects to hotel aggregator APIs (e.g., Bunkly).
Offers real-time availability, dynamic pricing, and filtering by proximity to TL circuits.

3. Ticket Booking Service 🎟️
Manages TL race ticket inventory and seat categories (Grandstand, VIP, General Admission).

CUSTOMER FEEDBACK
After each booking, a customer will be asked to fill in a questionaire.

CHAT BOT
A chat bot will answer the frequently asked questions.

OUR VISION
We believe life is meant to be lived at full throttle.
Not just seen, but felt. Not just remembered, but relived again and again.

MISSION
That’s why we craft once-in-a-lifetime Torque League journeys — where the roar of the engines meets the soul of the city. Where luxury travel and local culture collide with pure adrenaline. Where you don’t just watch the race… you become part of its story.

PRODUCTS

Target Market(s)

Affluent individuals, typically 35−65 years old, in professional, executive, or entrepreneurial roles. High net worth with significant disposable income.

Coding

Coded - Design and coding required

Number of Pages Required

5+ page

Requirements
Must have
• Central Package API
Nice to have
• Customer feedback after each booking , chat bot.

```html
<!DOCTYPE html>
<html lang="en">
<head>
<meta charset="utf-8">
<title>Kestrel Voyages Elite</title>
<link href="https://fonts.googleapis.com/css2?family=Outfit:wght@300;400;500;600;700&display=swap" rel="stylesheet">
<style>
:root{
  --red:#e1001a;
  --black:#0b0b0b;
  --ink:#1c1c1c;
  --muted:#6b6b6b;
  --light:#efefef;
  --line:#dcdcdc;
  --hotel-card:#4d4d4d;
  --star:#f5c518;
  --white:#fff;
}
*{box-sizing:border-box;margin:0;padding:0}
html,body{width:1200px;height:3906px;overflow:hidden}
body{font-family:'Outfit',sans-serif;color:var(--ink);background:var(--white);position:relative}
.btn-red{background:var(--red);color:#fff;font-weight:600;font-size:10px;border-radius:3px;display:inline-flex;align-items:center;justify-content:center}
.btn-outline{border:1px solid #333;background:#fff;color:#222;font-size:10px;font-weight:600;border-radius:3px;display:inline-flex;align-items:center;justify-content:center}

/* header + hero */
.hero{position:absolute;left:0;top:0;width:1200px;height:518px;background:var(--black);border-radius:0 0 70px 70px;overflow:hidden}
.hero-photo{position:absolute;inset:0;background:radial-gradient(ellipse at 70% 40%,#6a5448 0%,#2e2420 40%,#0b0b0b 80%)}
.site-header{position:absolute;top:0;left:0;width:1200px;height:40px;display:flex;align-items:center;padding:0 122px;color:#fff;border-bottom:1px solid #4a1a1a;z-index:2}
.brand{font-size:18px;font-weight:500}
.main-nav{display:flex;gap:22px;margin-left:132px;font-size:11px}
.account{display:flex;gap:22px;margin-left:auto;font-size:11px;align-items:center}
.account span{display:flex;align-items:center;gap:5px}
.header-cta{margin-left:18px;height:28px;width:86px;font-size:11px;font-weight:500}
.hero-title{position:absolute;top:112px;width:1200px;text-align:center;color:#fff;font-weight:300;font-size:48px;line-height:60px}
.hero-sub{position:absolute;top:232px;width:1200px;text-align:center;color:#eee;font-size:14px;line-height:18px}
.search{position:absolute;left:137px;top:417px;width:924px;height:100px;background:rgba(40,40,40,.85);border-radius:6px 6px 0 0}
.tabs{display:flex;gap:6px;padding:5px 12px}
.tabs span{width:62px;height:20px;display:flex;align-items:center;justify-content:center;color:#fff;font-size:11px;background:#3b3b3b}
.tabs .active{background:#888}
.fields{display:flex;gap:8px;padding:12px 17px}
.field{width:186px;height:33px;background:#fff;border-radius:2px;display:flex;align-items:center;justify-content:space-between;padding:0 12px;font-size:11px;color:#444}
.search-btn{width:123px;height:33px;font-size:11px;justify-content:space-between;padding:0 14px}

/* services */
.services{position:absolute;top:518px;left:0;width:1200px;height:377px;background:var(--light)}
.section-title{font-weight:300;font-size:33px}
.services .section-title{text-align:center;margin-top:50px}
.service-list{display:flex;justify-content:center;gap:78px;margin-top:28px}
.service{width:158px;text-align:center;position:relative}
.service-photo{width:158px;height:158px;border-radius:50%;border:3px solid var(--red);margin:0 auto}
.service-icon{position:absolute;left:-20px;top:58px;width:40px;height:40px;border-radius:50%;background:var(--red);border:3px solid #fff;display:flex;align-items:center;justify-content:center}
.service h3{font-weight:500;font-size:15px;margin-top:20px;white-space:nowrap}
.service p{font-size:10.5px;color:var(--muted);line-height:13px;margin:4px -20px 0}

/* featured */
.featured{position:absolute;left:0;width:1200px}
.featured-head{position:absolute;left:120px;right:122px;display:flex;justify-content:space-between;align-items:center}
.view-all{width:92px;height:32px}
.arrow{position:absolute;width:22px;height:22px;border-radius:50%;border:1.5px solid var(--red);display:flex;align-items:center;justify-content:center}
.cards{position:absolute;left:121px;display:flex;gap:12px}
.card{width:230px;height:259px;background:#fff;border:1px solid var(--line);padding:6px}
.card-photo{height:141px}
.card-body{padding:12px 8px 0}
.card-name{font-size:13px;line-height:16px;text-transform:uppercase}
.card-spec{font-size:9px;color:#444;line-height:12px;margin-top:2px}
.card-actions{display:flex;gap:5px;margin-top:12px;padding-left:4px}
.price{width:88px;height:25px;border:1px solid #888;border-radius:3px;display:flex;align-items:center;justify-content:center;font-size:13px}
.card-actions .btn-red{width:94px;height:25px}
.hotels{top:1327px;height:430px;background:var(--light)}
.hotel-card{background:var(--hotel-card);border:none;color:#fff;height:259px}
.pin-tag{display:inline-flex;align-items:center;gap:3px;background:#6c6c6c;font-size:8px;padding:2px 6px;border-radius:2px;margin-bottom:6px}
.hotel-card .card-name{text-transform:none}
.hotel-card .price{border-color:#ddd;color:#fff}
.ticket-card .card-name{text-transform:none}
.ticket-card .card-spec{font-size:8px;color:#666}

/* reviews */
.reviews{position:absolute;top:2180px;left:0;width:1200px;height:393px;background:linear-gradient(180deg,#1f3a35 0%,#27463a 45%,#1d3624 100%);color:#fff}
.reviews .section-title{text-align:center;margin-top:48px;font-size:32px}
.review{position:absolute;top:112px;width:330px}
.quote-mark{font-size:90px;line-height:60px;height:52px;color:transparent;-webkit-text-stroke:1.5px #cfcfcf;font-family:'Outfit',sans-serif}
.review p{font-size:12.5px;font-style:italic;line-height:17px;margin-top:12px}
.reviewer{display:flex;align-items:center;gap:10px;margin-top:30px}
.avatar{width:50px;height:50px;border-radius:50%;background:#cfd6e2;border:2px solid #fff}
.stars{color:var(--star);font-size:18px;letter-spacing:1px;line-height:18px}
.reviewer-name{font-size:13px;letter-spacing:.5px}
.reviewer-name small{font-size:11px}

/* vision */
.vision{position:absolute;top:2637px;left:121px;width:958px;height:284px;border:1px solid var(--line);background:#fff}
.vm{position:absolute;top:54px;width:230px}
.vm-icon{width:50px;height:50px;border-radius:50%;background:var(--red);display:flex;align-items:center;justify-content:center}
.vm h2{font-size:33px;font-weight:300;margin-top:12px}
.vm p{font-size:10.5px;color:var(--muted);line-height:14px;margin-top:6px}
.vision-photo{position:absolute;left:296px;top:5px;width:364px;height:272px}

/* packages */
.packages-title{position:absolute;top:2960px;width:1200px;text-align:center;font-size:33px;font-weight:300}
.packages{position:absolute;top:3025px;left:127px;display:flex;gap:13px}
.pkg{width:231px;height:257px;border:1px solid var(--line);padding:6px}
.pkg-photo{height:146px}
.pkg h3{font-size:14px;font-weight:500;margin:16px 5px 4px}
.pkg p{font-size:10px;color:var(--muted);line-height:13px;margin:0 5px}
.all-packages{position:absolute;top:3316px;left:547px;width:117px;height:30px;font-size:11px}

/* cta + footer */
.footer{position:absolute;top:3490px;left:0;width:1200px;height:416px;background:var(--black);border-radius:70px 0 0 0;color:#fff}
.cta{position:absolute;top:3401px;left:127px;width:957px;height:234px;background:var(--red);border-radius:10px;color:#fff;text-align:center;z-index:2}
.cta h2{font-weight:300;font-size:33px;line-height:38px;margin-top:48px}
.cta p{font-size:11px;margin-top:10px}
.cta-actions{display:flex;justify-content:center;gap:8px;margin-top:18px}
.cta-actions span{width:120px;height:32px;display:flex;align-items:center;justify-content:center;font-size:11px;font-weight:600;border-radius:3px}
.cta-light{background:#fff;color:#111}
.cta-dark{background:#111;color:#fff;width:156px!important}
.footer-cols{position:absolute;top:185px;left:127px;width:957px;display:flex}
.fcol{padding-right:20px}
.fcol h4{font-weight:400;font-size:16px;margin-bottom:14px}
.fcol p,.fcol li{font-size:9px;color:#bbb;line-height:14px;list-style:none}
.fcol.about{width:250px;border-right:1px solid #555;margin-right:80px}
.fcol.links{width:206px;border-right:1px solid #555}
.fcol.contact{width:256px;border-right:1px solid #555}
.fcol.social{padding-left:86px}
.row{display:flex;align-items:center;gap:12px;margin-bottom:12px;font-size:9px;color:#bbb}
.ring{width:22px;height:22px;border-radius:50%;border:1px solid #bbb;display:flex;align-items:center;justify-content:center}
.copy{position:absolute;top:395px;left:127px;width:957px;display:flex;justify-content:space-between;font-size:9px;color:#aaa;border-top:1px solid #444}
.copy .legal{display:flex;gap:14px}
</style>
</head>
<body>

<section class="hero">
  <div class="hero-photo" role="img" aria-label="Fans celebrating at a race with an air ticket in hand"></div>
  <header class="site-header">
    <div class="brand">Kestrel Voyages Elite</div>
    <nav class="main-nav"><span>Flight Tickets</span><span>Hotel Booking</span><span>Ticket Booking</span><span>Review</span><span>About</span></nav>
    <div class="account">
      <span><svg width="11" height="11" viewBox="0 0 12 12"><circle cx="6" cy="6" r="5" fill="none" stroke="#fff"/><circle cx="6" cy="5" r="2" fill="#fff"/></svg>Sign Up</span>
      <span><svg width="11" height="11" viewBox="0 0 12 12"><circle cx="6" cy="6" r="5" fill="none" stroke="#fff"/><circle cx="6" cy="5" r="2" fill="#fff"/></svg>Login</span>
    </div>
    <span class="btn-red header-cta">Contact Us</span>
  </header>
  <h1 class="hero-title">Experience Torque League<br>Like Never Before</h1>
  <p class="hero-sub">World-class race tickets, premium hospitality, seamless travel,<br>and curated experiences — feel the thrill of every destination.</p>
  <div class="search">
    <div class="tabs"><span class="active">Flight</span><span>Hotel</span><span>Ticket</span></div>
    <div class="fields">
      <div class="field">From <svg width="8" height="11" viewBox="0 0 8 11"><path d="M4 0a4 4 0 0 0-4 4c0 3 4 7 4 7s4-4 4-7a4 4 0 0 0-4-4z" fill="#333"/><circle cx="4" cy="4" r="1.4" fill="#fff"/></svg></div>
      <div class="field">To <svg width="8" height="11" viewBox="0 0 8 11"><path d="M4 0a4 4 0 0 0-4 4c0 3 4 7 4 7s4-4 4-7a4 4 0 0 0-4-4z" fill="#333"/><circle cx="4" cy="4" r="1.4" fill="#fff"/></svg></div>
      <div class="field">Date <svg width="9" height="9" viewBox="0 0 9 9"><rect x=".5" y="1" width="8" height="7.5" fill="none" stroke="#333"/><path d="M.5 3h8" stroke="#333"/></svg></div>
      <div class="field">PAX <svg width="9" height="6" viewBox="0 0 9 6"><path d="M1 1l3.5 3.5L8 1" fill="none" stroke="#333"/></svg></div>
      <span class="btn-red search-btn">Search <svg width="10" height="10" viewBox="0 0 10 10"><circle cx="4" cy="4" r="3" fill="none" stroke="#fff" stroke-width="1.3"/><path d="M6.3 6.3L9 9" stroke="#fff" stroke-width="1.3"/></svg></span>
    </div>
  </div>
</section>

<section class="services">
  <h2 class="section-title">Services We Offer</h2>
  <div class="service-list">
    <div class="service">
      <div class="service-photo" role="img" aria-label="Hand holding a phone with a flight booking app" style="background:radial-gradient(circle,#9aa7b5,#4d5a66)"></div>
      <div class="service-icon"><svg width="18" height="18" viewBox="0 0 24 24"><path d="M21 16v-2l-8-5V3.5a1.5 1.5 0 0 0-3 0V9l-8 5v2l8-2.5V19l-2 1.5V22l3.5-1 3.5 1v-1.5L13 19v-5.5z" fill="#fff"/></svg></div>
      <h3>Flight Booking Service</h3>
      <p>Real-time availability, multiple classes, global flight partners.</p>
    </div>
    <div class="service">
      <div class="service-photo" role="img" aria-label="Laptop with a hotel booking screen" style="background:radial-gradient(circle,#c9d6e3,#7d8a98)"></div>
      <div class="service-icon"><svg width="18" height="18" viewBox="0 0 24 24"><path d="M3 18V8h2v5h6V9h7a3 3 0 0 1 3 3v6h-2v-2H5v2z" fill="#fff"/><circle cx="8" cy="11" r="1.8" fill="#fff"/></svg></div>
      <h3>Hotel Booking Service</h3>
      <p>Real-time availability, multiple classes, global flight partners.</p>
    </div>
    <div class="service">
      <div class="service-photo" role="img" aria-label="Event tickets on a keyboard" style="background:radial-gradient(circle,#d7dde6,#8c97a6)"></div>
      <div class="service-icon"><svg width="18" height="18" viewBox="0 0 24 24"><path d="M3 7h18v3a2 2 0 0 0 0 4v3H3v-3a2 2 0 0 0 0-4z" fill="#fff"/></svg></div>
      <h3>Ticket Booking Service</h3>
      <p>Real-time availability, multiple classes, global flight partners.</p>
    </div>
  </div>
</section>

<section class="featured" style="top:895px;height:432px">
  <div class="featured-head" style="top:42px"><h2 class="section-title">Featured Flights</h2><span class="btn-outline view-all">View All</span></div>
  <span class="arrow" style="left:78px;top:235px"><svg width="10" height="10" viewBox="0 0 10 10"><path d="M9 5H1M4 2L1 5l3 3" fill="none" stroke="#e1001a" stroke-width="1.3"/></svg></span>
  <span class="arrow" style="left:1098px;top:235px"><svg width="10" height="10" viewBox="0 0 10 10"><path d="M1 5h8M6 2l3 3-3 3" fill="none" stroke="#e1001a" stroke-width="1.3"/></svg></span>
  <div class="cards" style="top:117px">
    <div class="card"><div class="card-photo" role="img" aria-label="Passenger jet taking off against a blue sky" style="background:linear-gradient(180deg,#7fa8cf,#c6d9ea)"></div><div class="card-body"><div class="card-name">SKYLARK-580-KVE</div><div class="card-spec">Speed: 411 mph<br>Range: 1523 mi</div><div class="card-actions"><span class="price">$5,000</span><span class="btn-red">View Packages</span></div></div></div>
    <div class="card"><div class="card-photo" role="img" aria-label="Turboprop plane on a runway" style="background:linear-gradient(180deg,#c9dbe8 0%,#b9c9a8 70%,#8b8f77 100%)"></div><div class="card-body"><div class="card-name">ALPINA-AX-14</div><div class="card-spec">Speed: 411 mph<br>Range: 1523 mi</div><div class="card-actions"><span class="price">$5,000</span><span class="btn-red">View Packages</span></div></div></div>
    <div class="card"><div class="card-photo" role="img" aria-label="White business jet on tarmac" style="background:linear-gradient(180deg,#aac3db 0%,#dde3e8 60%,#9a9a9a 100%)"></div><div class="card-body"><div class="card-name">ZEPHYRJET</div><div class="card-spec">Speed: 411 mph<br>Range: 1523 mi</div><div class="card-actions"><span class="price">$5,000</span><span class="btn-red">View Packages</span></div></div></div>
    <div class="card"><div class="card-photo" role="img" aria-label="Private jet in flight against a grey sky" style="background:linear-gradient(180deg,#b9b9b9,#e2e2e2)"></div><div class="card-body"><div class="card-name">SKYLARK-580-KVE</div><div class="card-spec">Speed: 411 mph<br>Range: 1523 mi</div><div class="card-actions"><span class="price">$5,000</span><span class="btn-red">View Packages</span></div></div></div>
  </div>
</section>

<section class="featured hotels">
  <div class="featured-head" style="top:52px"><h2 class="section-title">Featured Hotes</h2><span class="btn-outline view-all">View All</span></div>
  <span class="arrow" style="left:78px;top:237px"><svg width="10" height="10" viewBox="0 0 10 10"><path d="M9 5H1M4 2L1 5l3 3" fill="none" stroke="#e1001a" stroke-width="1.3"/></svg></span>
  <span class="arrow" style="left:1098px;top:237px"><svg width="10" height="10" viewBox="0 0 10 10"><path d="M1 5h8M6 2l3 3-3 3" fill="none" stroke="#e1001a" stroke-width="1.3"/></svg></span>
  <div class="cards" style="top:116px">
    <div class="card hotel-card"><div class="card-photo" role="img" aria-label="Hillside resort at sunset" style="background:linear-gradient(180deg,#e8a24a 0%,#c77a4a 45%,#5a5a4a 100%)"></div><div class="card-body"><span class="pin-tag">⚲ Candolim</span><div class="card-name">Saffron Hills Retreat -<br>Luxury Stay Naini</div><div class="card-actions"><span class="price">€1.769,01</span><span class="btn-red">View Packages</span></div></div></div>
    <div class="card hotel-card"><div class="card-photo" role="img" aria-label="Infinity pool overlooking the sea" style="background:linear-gradient(180deg,#7ec3e0 0%,#3a8fd0 60%,#1f5fa8 100%)"></div><div class="card-body"><span class="pin-tag">⚲ Candolim</span><div class="card-name">Nordlys Harbour Hotel,<br>Copenhagen</div><div class="card-actions"><span class="price">€1.769,01</span><span class="btn-red">View Packages</span></div></div></div>
    <div class="card hotel-card"><div class="card-photo" role="img" aria-label="Warmly lit hotel bedroom" style="background:linear-gradient(180deg,#d8c5a6 0%,#b89a72 60%,#e9e1d4 100%)"></div><div class="card-body"><span class="pin-tag">⚲ Candolim</span><div class="card-name">Saffron Hills Retreat -<br>Luxury Stay Naini</div><div class="card-actions"><span class="price">€1.769,01</span><span class="btn-red">View Packages</span></div></div></div>
    <div class="card hotel-card"><div class="card-photo" role="img" aria-label="Hotel courtyard with a pool and parasols" style="background:linear-gradient(180deg,#b9cde0 0%,#d8cbb8 45%,#5fa6c4 100%)"></div><div class="card-body"><span class="pin-tag">⚲ Candolim</span><div class="card-name">Lindgren Apartment Hotel<br>Copenhagen</div><div class="card-actions"><span class="price">€1.769,01</span><span class="btn-red">View Packages</span></div></div></div>
  </div>
</section>

<section class="featured" style="top:1757px;height:423px">
  <div class="featured-head" style="top:46px"><h2 class="section-title">Featured Tickets</h2><span class="btn-outline view-all">View All</span></div>
  <span class="arrow" style="left:78px;top:232px"><svg width="10" height="10" viewBox="0 0 10 10"><path d="M9 5H1M4 2L1 5l3 3" fill="none" stroke="#e1001a" stroke-width="1.3"/></svg></span>
  <span class="arrow" style="left:1098px;top:232px"><svg width="10" height="10" viewBox="0 0 10 10"><path d="M1 5h8M6 2l3 3-3 3" fill="none" stroke="#e1001a" stroke-width="1.3"/></svg></span>
  <div class="cards" style="top:115px">
    <div class="card ticket-card"><div class="card-photo" role="img" aria-label="Light trails on a night circuit" style="background:linear-gradient(180deg,#1e3a8a 0%,#3b5fc0 40%,#c0902e 70%,#4a5a2a 100%)"></div><div class="card-body"><div class="card-name">2025 Silver Coast<br>Grand Prix</div><div class="card-spec">Thursday - Saturday.</div><div class="card-actions"><span class="price">€1.769,01</span><span class="btn-red">On Sale Now</span></div></div></div>
    <div class="card ticket-card"><div class="card-photo" role="img" aria-label="Floodlit grandstand at night" style="background:linear-gradient(180deg,#0d1740 0%,#3a4a8a 50%,#a8302a 80%,#d9c9a0 100%)"></div><div class="card-body"><div class="card-name">Rowan Hale<br>Grandstand 3-Days</div><div class="card-spec">Thursday - Saturday.</div><div class="card-actions"><span class="price">€985,59</span><span class="btn-red">View Packages</span></div></div></div>
    <div class="card ticket-card"><div class="card-photo" role="img" aria-label="Stadium seats with a lone spectator" style="background:linear-gradient(180deg,#8a9aa8 0%,#b8c0c4 40%,#5a9a7a 70%,#c8c8c8 100%)"></div><div class="card-body"><div class="card-name">Rowan Hale Grandstand<br>Middle Rows 3-Days</div><div class="card-spec">Thursday - Saturday.</div><div class="card-actions"><span class="price">€1.167,55</span><span class="btn-red">View Packages</span></div></div></div>
    <div class="card ticket-card"><div class="card-photo" role="img" aria-label="Runner on a stadium track" style="background:linear-gradient(180deg,#7a8a6a 0%,#9aa0a4 40%,#6a6e72 100%)"></div><div class="card-body"><div class="card-name">2025 Highland Mesa<br>Grand Prix</div><div class="card-spec">Thursday - Saturday.</div><div class="card-actions"><span class="price">€1.769,01</span><span class="btn-red">View Packages</span></div></div></div>
  </div>
</section>

<section class="reviews" role="img" aria-label="Traveller with a backpack overlooking a misty green valley">
  <h2 class="section-title">Customer Review</h2>
  <span class="arrow" style="left:78px;top:200px;border-color:#fff"><svg width="10" height="10" viewBox="0 0 10 10"><path d="M9 5H1M4 2L1 5l3 3" fill="none" stroke="#fff" stroke-width="1.3"/></svg></span>
  <span class="arrow" style="left:1098px;top:200px;border-color:#fff"><svg width="10" height="10" viewBox="0 0 10 10"><path d="M1 5h8M6 2l3 3-3 3" fill="none" stroke="#fff" stroke-width="1.3"/></svg></span>
  <div class="review" style="left:127px">
    <div class="quote-mark">“</div>
    <p>“Lorem ipsum dolor sit amet, consectetur adipiscing elit. Donec dignissim laoreet orci ac elementum. Nam lectus ipsum, feugiat id purus finibus, venenatis molestie justo. Vestibulum maximus felis vitae finibus semper. Curabitur eget dui sed sapien cursus volutpat id sit amet quam.”</p>
    <div class="reviewer"><div class="avatar"></div><div><div class="stars">★★★★★</div><div class="reviewer-name">Aarav Mehta, <small>Our Client</small></div></div></div>
  </div>
  <div class="review" style="left:745px">
    <div class="quote-mark">“</div>
    <p>“Lorem ipsum dolor sit amet, consectetur adipiscing elit. Donec dignissim laoreet orci ac elementum. Nam lectus ipsum, feugiat id purus finibus, venenatis molestie justo. Vestibulum maximus felis vitae finibus semper. Curabitur eget dui sed sapien cursus volutpat id sit amet quam.”</p>
    <div class="reviewer"><div class="avatar"></div><div><div class="stars">★★★★★</div><div class="reviewer-name">Aarav Mehta, <small>Our Client</small></div></div></div>
  </div>
</section>

<section class="vision">
  <div class="vm" style="left:28px">
    <div class="vm-icon"><svg width="26" height="26" viewBox="0 0 24 24"><path d="M1 12s4-7 11-7 11 7 11 7-4 7-11 7S1 12 1 12z" fill="#fff"/><circle cx="12" cy="12" r="4" fill="#e1001a"/><circle cx="12" cy="12" r="1.8" fill="#fff"/></svg></div>
    <h2>Our Vision</h2>
    <p>We believe life is meant to be lived at full throttle. Not just seen, but felt. Not just remembered, but relived again and again.</p>
  </div>
  <div class="vision-photo" role="img" aria-label="Hand placing a dart on a target" style="background:linear-gradient(135deg,#9aa2ac 0%,#6a727c 50%,#c2a24a 100%)"></div>
  <div class="vm" style="left:692px">
    <div class="vm-icon"><svg width="26" height="26" viewBox="0 0 24 24"><circle cx="11" cy="13" r="8" fill="none" stroke="#fff" stroke-width="2"/><circle cx="11" cy="13" r="4" fill="none" stroke="#fff" stroke-width="2"/><path d="M11 13L20 4M17 4h3v3" stroke="#fff" stroke-width="2" fill="none"/></svg></div>
    <h2>Our Mission</h2>
    <p>That’s why we craft once-in-a-lifetime Torque League journeys — where the roar of the engines meets the soul of the city. Where luxury travel and local culture collide with pure adrenaline. Where you don’t just watch the race…you become part of its story.</p>
  </div>
</section>

<h2 class="packages-title">Exclusive Torque League travel Packages</h2>
<div class="packages">
  <div class="pkg"><div class="pkg-photo" role="img" aria-label="Globe and compass on a desk with tickets" style="background:linear-gradient(135deg,#3a3a3a,#7a8a9a 60%,#d8d8d8)"></div><h3>World-Class Tickets</h3><p>Secure the best seats in the house — from Grandstand to VIP Paddock access. Every package guarantees an unforgettable race-day experience.</p></div>
  <div class="pkg"><div class="pkg-photo" role="img" aria-label="Hospitality host in an elegant lounge" style="background:linear-gradient(135deg,#e8e0d2,#c8b89a 60%,#4a4a4a)"></div><h3>Premium Hospitality</h3><p>Enjoy gourmet dining, exclusive lounges, and behind-the-scenes access designed for the discerning traveler.</p></div>
  <div class="pkg"><div class="pkg-photo" role="img" aria-label="Travellers reading a map in a historic square" style="background:linear-gradient(135deg,#c9a27a,#b0705a 50%,#e2d2b8)"></div><h3>Seamless Travel</h3><p>Flights and hotels are fully integrated into your package. Travel with ease and style, with accommodations chosen for comfort, location, &amp; luxury.</p></div>
  <div class="pkg"><div class="pkg-photo" role="img" aria-label="Smiling guest with a five-star rating board" style="background:linear-gradient(135deg,#2a2a2a,#6a5a4a 55%,#d8c2a0)"></div><h3>Curated Experiences</h3><p>Go beyond the track — private tours, cultural excursions, and unique local experiences that make each destination unforgettable.</p></div>
</div>
<span class="btn-red all-packages">View all Packages</span>

<section class="cta">
  <h2>Turn Every Grand Prix Into<br>a Onc in-a-Lifetime Journey”</h2>
  <p>From Monaco to Abu Dhabi, we make every moment count.</p>
  <div class="cta-actions"><span class="cta-light">Explore Packages</span><span class="cta-dark">Contact Our Concierge</span></div>
</section>

<footer class="footer">
  <div class="footer-cols">
    <div class="fcol about"><h4>Kestrel Voyages Elite</h4><p>Not just seen, but felt. Not just remembered, but relived again and again. That’s why we craft once-in-a-lifetime Torque League journeys — where the roar of the engines meets the soul of the city, and luxury travel meets local culture.</p></div>
    <div class="fcol links"><h4>Quick links</h4><ul><li>Flight Tickets</li><li>Hotel Booking</li><li>Ticket Booking</li><li>Review</li><li>About</li><li>Contact us</li></ul></div>
    <div class="fcol contact"><h4>Contact Us</h4>
      <div class="row"><span class="ring"><svg width="10" height="10" viewBox="0 0 24 24"><path d="M6.6 10.8a15 15 0 0 0 6.6 6.6l2.2-2.2c.3-.3.7-.4 1-.2 1.1.4 2.3.6 3.6.6.6 0 1 .4 1 1V20c0 .6-.4 1-1 1A17 17 0 0 1 3 4c0-.6.4-1 1-1h3.5c.6 0 1 .4 1 1 0 1.3.2 2.5.6 3.6.1.3 0 .7-.2 1z" fill="#fff"/></svg></span>1-800-555-0142</div>
      <div class="row"><span class="ring"><svg width="10" height="10" viewBox="0 0 24 24"><rect x="2" y="5" width="20" height="14" fill="none" stroke="#fff" stroke-width="2"/><path d="M2 5l10 8 10-8" fill="none" stroke="#fff" stroke-width="2"/></svg></span><span style="color:var(--red)">info@kestrelvoyages.com</span></div>
    </div>
    <div class="fcol social"><h4>Follow us</h4>
      <div class="row"><span class="ring"></span>Friendline</div>
      <div class="row"><span class="ring"></span>Chirper</div>
      <div class="row"><span class="ring"></span>Linkwork</div>
    </div>
  </div>
  <div class="copy"><span>© Copyright 2025 Kestrel Voyages Elite All Rights Reserved.</span><span class="legal"><span>Terms and Conditions</span><span>|</span><span>Privacy Policy</span><span>|</span><span>Sitemap</span></span></div>
</footer>

</body>
</html>
```